Kelvane Plumbing Business cards

Company is Kelvane Plumbing.
name Dashel Morrowby, I am a plumber, drainer, gasfitter and roofer
Mobile: 0431 906 154
Email address: info@kelvaneplumbing.example (check out my website for some ideas)
Website: www.kelvaneplumbing.example
ABN: 82 916 203 471
LIC: 604517K

I am reliable all round plumber. I am a 24 hour emergency service. Kelvane Plumbing is a professional plumbing service in the Illawarra, South Coast, Southern Sydney and Southern Highland regions of NSW. We offer a 24 hour emergency service for piece of mind to our customers. Call us now to see how we can help you. Kelvane Plumbing approaches every job with attention to detail and excellent customer service. With our superior workmanship you can be confident that the job will be done right the first time around. You can rest assured with results that are guaranteed to last.

Target Market(s)

the general public

Contact Information for Business Card

look up website for some ideas something with similar colours to logo and new modern and to catch the eye.

Colors
fdfdfd
ffffff
000000
7f7f7f
aaaaaa
33a6d7
0492cd

Requirements
Must have
• all contact details
• company- Kelvane Plumbing
• name- Dashel Morrowby
• number mobile- 0431 906 154
• Email address- info@kelvaneplumbing.example
• Website- www.kelvaneplumbing.example
• ABN- 82 916 203 471
• LIC- 604517K

```html
<!DOCTYPE html>
<html lang="en">
<head>
<meta charset="utf-8">
<title>Kelvane Plumbing – Business Cards</title>
<link rel="stylesheet" href="https://fonts.googleapis.com/css2?family=Fira+Sans+Condensed:ital,wght@0,400;0,700;1,400;1,700&family=Work+Sans:wght@400;500&display=swap">
<style>
  :root {
    --bg: #1c1c1c;
    --card: #222222;
    --card-edge: #2a2a2a;
    --blue: #1f9bd1;
    --grey: #7f7f7f;
    --light-grey: #aaaaaa;
    --white: #fdfdfd;
  }
  * { margin: 0; padding: 0; box-sizing: border-box; }
  html, body {
    width: 1200px; height: 900px; overflow: hidden;
    background: var(--bg);
  }
  .sheet {
    position: relative; width: 1200px; height: 900px;
    display: flex; flex-direction: column; align-items: center; justify-content: center; gap: 48px;
  }
  .card {
    position: relative; width: 640px; height: 366px;
    background: var(--card);
    border: 1px solid var(--card-edge);
    overflow: hidden;
    font-family: "Work Sans", sans-serif;
    color: var(--white);
  }

  /* Front */
  .card-front { display: flex; align-items: center; justify-content: center; gap: 16px; }
  .brand-mark {
    width: 34px; height: 34px; border-radius: 50%;
    border: 5px solid var(--blue);
  }
  .brand-name {
    font-family: "Work Sans", sans-serif; font-weight: 500;
    font-size: 30px; letter-spacing: 2px; text-transform: uppercase;
    color: var(--blue);
  }

  /* Back */
  .back-brand {
    position: absolute; right: 40px; top: 36px;
    font-weight: 500; font-size: 22px; letter-spacing: 1.5px;
    text-transform: uppercase; color: var(--blue);
  }
  .person { position: absolute; left: 40px; top: 82px; }
  .person-name {
    font-family: "Fira Sans Condensed", sans-serif; font-weight: 700; font-style: italic;
    font-size: 32px; letter-spacing: 1px; text-transform: uppercase; color: var(--blue);
    line-height: 1;
  }
  .person-role {
    font-family: "Fira Sans Condensed", sans-serif; font-style: italic;
    font-size: 16px; margin-top: 6px; color: var(--white);
  }
  .divider {
    position: absolute; left: 40px; right: 40px; top: 168px;
    height: 1.5px; background: var(--blue);
  }
  .registration {
    position: absolute; right: 40px; top: 108px; text-align: right;
    font-size: 17px; line-height: 1.5; letter-spacing: .5px;
  }
  .registration .label { color: var(--blue); }
  .contact-list {
    position: absolute; left: 40px; top: 186px; list-style: none;
    font-size: 17px; line-height: 1.6;
  }
  .contact-list li { display: flex; align-items: center; gap: 10px; }
  .contact-list svg { width: 14px; height: 14px; flex: none; }
  .address {
    position: absolute; right: 40px; top: 262px; text-align: right;
    font-size: 18px; line-height: 1.4; letter-spacing: .5px;
  }
  .footer-band { position: absolute; left: 0; bottom: 0; width: 640px; height: 56px; }
</style>
</head>
<body>
<main class="sheet">

  <section class="card card-front" aria-label="Card front">
    <span class="brand-mark" aria-hidden="true"></span>
    <span class="brand-name">Kelvane Plumbing</span>
  </section>

  <section class="card card-back" aria-label="Card back">
    <div class="back-brand">Kelvane Plumbing</div>

    <div class="person">
      <h1 class="person-name">Dashel Morrowby</h1>
      <p class="person-role">Plumber, Drainer, Gasfitter And Roofer</p>
    </div>

    <div class="registration">
      <div><span class="label">ABN</span> - 82 916 203 471</div>
      <div><span class="label">LIC</span> - 604517K</div>
    </div>

    <div class="divider"></div>

    <ul class="contact-list">
      <li>
        <svg viewBox="0 0 24 24" fill="none" stroke="#1f9bd1" stroke-width="2"><path d="M5 3h4l2 5-3 2a11 11 0 0 0 6 6l2-3 5 2v4a2 2 0 0 1-2 2A17 17 0 0 1 3 5a2 2 0 0 1 2-2z"/></svg>
        0431 906 154
      </li>
      <li>
        <svg viewBox="0 0 24 24" fill="none" stroke="#1f9bd1" stroke-width="2"><rect x="3" y="5" width="18" height="14" rx="1"/><path d="M3 6l9 7 9-7"/></svg>
        info@kelvaneplumbing.example
      </li>
      <li>
        <svg viewBox="0 0 24 24" fill="none" stroke="#1f9bd1" stroke-width="2"><circle cx="12" cy="12" r="9"/><path d="M3 12h18M12 3c3 3 3 15 0 18M12 3c-3 3-3 15 0 18"/></svg>
        www.kelvaneplumbing.example
      </li>
    </ul>

    <address class="address" style="font-style:normal">
      412c Marrin Street,<br>Ashcombe, NZ, 8042
    </address>

    <svg class="footer-band" viewBox="0 0 640 56" aria-hidden="true">
      <path d="M0 20 L370 20 L392 28 L0 28 Z" fill="#7f7f7f"/>
      <path d="M0 36 L390 36 C410 36 412 24 440 24 L640 24 L640 56 L0 56 Z" fill="#1f9bd1"/>
    </svg>
  </section>

</main>
</body>
</html>
```